Need new sign at entrance for new fruit and vegetable wholesaler in market. Main vegetables sold are
Broccoli , Cauliflower , cabbage , capsicum , tomatoes , lettuce .
Business name is Tenby Crop
I have included examples of other designs and a sketch of suggested layout.
Business

```html
<!DOCTYPE html>
<html lang="en">
<head>
<meta charset="utf-8">
<title>Tenby Crop – Entrance Sign</title>
<link rel="stylesheet" href="https://fonts.googleapis.com/css2?family=Fira+Sans+Condensed:wght@400;500&display=swap">
<style>
  :root {
    --page: #ffffff;
    --lime: #a8cf38;
    --lime-deep: #6cbb45;
    --lime-light: #b9d94a;
    --ink: #ffffff;
    --broccoli-a: #3f7a1f;
    --broccoli-b: #9fc36a;
    --cabbage-a: #2f4d12;
    --cabbage-b: #c9d84a;
    --tomato-a: #e23a1c;
    --tomato-b: #f3d9c0;
  }
  * { margin: 0; padding: 0; box-sizing: border-box; }
  html, body {
    width: 1200px;
    height: 1000px;
    overflow: hidden;
    background: var(--page);
  }
  .canvas {
    position: relative;
    width: 1200px;
    height: 1000px;
    font-family: "Fira Sans Condensed", "Arial Narrow", sans-serif;
  }
  .sign {
    position: absolute;
    left: 0;
    top: 390px;
    width: 1200px;
    height: 217px;
    display: flex;
  }
  .brand-panel {
    width: 455px;
    height: 100%;
    background: linear-gradient(110deg, var(--lime-deep) 0%, var(--lime) 45%, var(--lime-light) 100%);
    display: flex;
    align-items: center;
    justify-content: center;
  }
  .brand-name {
    color: var(--ink);
    font-weight: 500;
    font-size: 78px;
    line-height: 1;
    letter-spacing: 1px;
  }
  .produce {
    display: flex;
    width: 420px;
    height: 100%;
  }
  .produce-tile { width: 140px; height: 100%; }
  .produce-tile.broccoli { background: linear-gradient(120deg, var(--broccoli-b) 0%, var(--broccoli-a) 55%, #5d8f2c 100%); }
  .produce-tile.cabbage { background: radial-gradient(circle at 50% 55%, var(--cabbage-b) 0%, #8fa82c 40%, var(--cabbage-a) 90%); }
  .produce-tile.tomato { background: linear-gradient(180deg, var(--tomato-a) 0%, #d8321a 65%, var(--tomato-b) 100%); }
  .info-panel {
    flex: 1;
    height: 100%;
    background: var(--lime);
    color: var(--ink);
    text-align: right;
    padding: 12px 28px 0 0;
  }
  .stand {
    font-size: 27px;
    font-weight: 500;
    line-height: 31px;
  }
  .contact {
    margin-top: 38px;
    font-size: 24px;
    line-height: 30px;
  }
</style>
</head>
<body>
  <main class="canvas">
    <section class="sign">
      <div class="brand-panel">
        <span class="brand-name">Tenby Crop</span>
      </div>
      <div class="produce">
        <div class="produce-tile broccoli" role="img" aria-label="Photo of fresh broccoli"></div>
        <div class="produce-tile cabbage" role="img" aria-label="Photo of a savoy cabbage"></div>
        <div class="produce-tile tomato" role="img" aria-label="Photo of red tomatoes in a woven basket"></div>
      </div>
      <div class="info-panel">
        <p class="stand">STAND 214<br>D SHED</p>
        <p class="contact">www.tenbycrop.com.au<br>Phone - 02 5550 1928<br>Fax - 02 5550 1928</p>
      </div>
    </section>
  </main>
</body>
</html>
```